Corvane

I'm looking for business cards with the logo I've attached. I don't have an specific idea in mind and open to anything. All the usual info will be involved. Name, position in company, nr, email, address

```html
<!DOCTYPE html>
<html lang="en">
<head>
<meta charset="utf-8">
<title>Corvane — Business Cards</title>
<link rel="stylesheet" href="https://fonts.googleapis.com/css2?family=Montserrat:wght@400;500;600;800&display=swap">
<style>
  :root {
    --navy: #172a4a;
    --gold: #e9a51f;
    --paper: #ffffff;
    --page: #ffffff;
    --ink-grey: #555a63;
    --faint: #dcdcdc;
    --shadow: rgba(0, 0, 0, 0.28);
  }
  * { box-sizing: border-box; margin: 0; padding: 0; }
  html, body {
    width: 713px;
    height: 1200px;
    overflow: hidden;
    background: var(--page);
    font-family: "Montserrat", sans-serif;
  }
  .sheet {
    position: relative;
    width: 713px;
    height: 1200px;
  }
  .card {
    position: absolute;
    left: 56px;
    width: 600px;
    height: 343px;
    background: var(--paper);
    overflow: hidden;
    box-shadow: 0 4px 10px var(--shadow);
  }
  .card--front { top: 227px; }
  .card--back { top: 630px; }

  .brand-mark {
    position: absolute;
    border-radius: 50%;
    background: var(--navy);
  }

  /* Front */
  .front-panel {
    position: absolute;
    inset: 0;
    width: 100%;
    height: 100%;
  }
  .front-mark {
    left: 423px;
    top: 48px;
    width: 60px;
    height: 60px;
  }
  .front-brand {
    position: absolute;
    left: 453px;
    top: 138px;
    transform: translateX(-50%);
    color: var(--gold);
    font-weight: 600;
    font-size: 42px;
    letter-spacing: 1px;
    line-height: 1;
  }
  .front-web {
    position: absolute;
    left: 325px;
    right: 0;
    top: 251px;
    height: 16px;
    background: var(--gold);
    color: var(--navy);
    font-weight: 600;
    font-size: 10.5px;
    letter-spacing: 3.4px;
    line-height: 16px;
    padding-left: 37px;
  }

  /* Back */
  .back-bar {
    position: absolute;
    left: 0; top: 0; bottom: 0;
    width: 53px;
    background: var(--navy);
  }
  .back-decor {
    position: absolute;
    left: 264px;
    top: 45px;
    width: 336px;
    height: 225px;
  }
  .back-mark {
    left: 124px;
    top: 32px;
    width: 44px;
    height: 44px;
  }
  .back-brand {
    position: absolute;
    left: 146px;
    top: 97px;
    transform: translateX(-50%);
    color: var(--gold);
    font-weight: 600;
    font-size: 30px;
    letter-spacing: 0.5px;
    line-height: 1;
  }
  .holder-name {
    position: absolute;
    left: 70px;
    top: 190px;
    color: var(--navy);
    font-weight: 800;
    font-size: 22px;
    letter-spacing: 0.2px;
  }
  .contact-list {
    position: absolute;
    left: 68px;
    top: 240px;
    list-style: none;
  }
  .contact-item {
    display: flex;
    align-items: center;
    height: 22px;
    color: var(--ink-grey);
    font-size: 13px;
    font-weight: 500;
    letter-spacing: 0.3px;
  }
  .contact-icon {
    width: 12px;
    height: 12px;
    margin-right: 11px;
    fill: var(--gold);
  }
  .web-pill {
    position: absolute;
    left: 408px;
    right: 0;
    top: 285px;
    height: 24px;
    background: var(--gold);
    border-radius: 12px 0 0 12px;
    display: flex;
    align-items: center;
    padding-left: 12px;
    color: var(--navy);
    font-weight: 600;
    font-size: 13px;
  }
  .web-icon {
    width: 13px;
    height: 13px;
    margin-right: 8px;
  }
</style>
</head>
<body>
<main class="sheet">

  <section class="card card--front" aria-label="Business card front">
    <svg class="front-panel" viewBox="0 0 600 343" preserveAspectRatio="none">
      <defs>
        <radialGradient id="emblem-glow" cx="50%" cy="55%" r="55%">
          <stop offset="0%" stop-color="#e9a51f" stop-opacity="0.85"/>
          <stop offset="100%" stop-color="#e9a51f" stop-opacity="0"/>
        </radialGradient>
        <clipPath id="navy-wedge">
          <polygon points="0,0 136,0 391,343 0,343"/>
        </clipPath>
      </defs>
      <polygon points="0,0 136,0 391,343 0,343" fill="var(--navy)" aria-hidden="true"/>
      <g clip-path="url(#navy-wedge)" role="img" aria-label="Large brand emblem decoration in gold on the navy panel">
        <ellipse cx="145" cy="170" rx="150" ry="115" fill="url(#emblem-glow)"/>
      </g>
    </svg>
    <div class="brand-mark front-mark" aria-hidden="true"></div>
    <div class="front-brand">CORVANE</div>
    <div class="front-web">WWW.YOURSITE.COM</div>
  </section>

  <section class="card card--back" aria-label="Business card back">
    <div class="back-bar"></div>
    <svg class="back-decor" viewBox="0 0 336 225" role="img" aria-label="Faint brand emblem decoration in light grey">
      <defs>
        <radialGradient id="faint-glow" cx="60%" cy="55%" r="55%">
          <stop offset="0%" stop-color="#dcdcdc" stop-opacity="0.9"/>
          <stop offset="100%" stop-color="#dcdcdc" stop-opacity="0"/>
        </radialGradient>
      </defs>
      <ellipse cx="200" cy="125" rx="180" ry="110" fill="url(#faint-glow)"/>
    </svg>
    <div class="brand-mark back-mark" aria-hidden="true"></div>
    <div class="back-brand">CORVANE</div>
    <h1 class="holder-name">YOUR NAME</h1>
    <ul class="contact-list">
      <li class="contact-item">
        <svg class="contact-icon" viewBox="0 0 24 24" aria-hidden="true"><path d="M6.6 10.8a15.2 15.2 0 0 0 6.6 6.6l2.2-2.2c.3-.3.7-.4 1-.2 1.1.4 2.3.6 3.6.6.6 0 1 .4 1 1V20c0 .6-.4 1-1 1A17 17 0 0 1 3 4c0-.6.4-1 1-1h3.5c.6 0 1 .4 1 1 0 1.3.2 2.5.6 3.6.1.3 0 .7-.2 1z"/></svg>
        02 5550 17400
      </li>
      <li class="contact-item">
        <svg class="contact-icon" viewBox="0 0 24 24" aria-hidden="true"><path d="M2 5h20v14H2z"/><path d="M3 6.5l9 6 9-6" fill="none" stroke="#fff" stroke-width="1.8"/></svg>
        your@mail.com
      </li>
      <li class="contact-item">
        <svg class="contact-icon" viewBox="0 0 24 24" aria-hidden="true"><path d="M12 2a7 7 0 0 0-7 7c0 5 7 13 7 13s7-8 7-13a7 7 0 0 0-7-7zm0 9.5A2.5 2.5 0 1 1 12 6.5a2.5 2.5 0 0 1 0 5z"/></svg>
        your address goes here
      </li>
    </ul>
    <div class="web-pill">
      <svg class="web-icon" viewBox="0 0 24 24" aria-hidden="true" fill="none" stroke="var(--navy)" stroke-width="2.4">
        <circle cx="12" cy="12" r="10"/>
        <ellipse cx="12" cy="12" rx="4.5" ry="10"/>
        <line x1="2" y1="12" x2="22" y2="12"/>
      </svg>
      www.yousite.com
    </div>
  </section>

</main>
</body>
</html>
```